Kestrel Building Works Business Card and more!

We need a business card design for Kestrel Building Works Ltd, a respected building company that specialises in high quality designer homes.

We're after a sleek, clean, modern business card that incorporates our new logo (see attached) and colours, with black being the background.

We are Certified Framing Guild and need to include their logo (see attached) on our cards, balancing but not taking over our logo.

Details to be included:

Malcolm Tivey
Director

Phone: 0218845126
Email: kestrelbuild.nz@maildrop-example.co.nz
Website: www.kestrelbuildingworks-example.co.nz

Additional Information

A start up website is also under construction and needing attention and letterheads are needed!

We look forward to your designs!

Target Market(s)

30+ people who are interested in building new or renovating current homes

Industry/Entity Type

Construction

Contact Information for Business Card

Malcolm Tivey
Director

Phone: 0218845126
Facebook: www.socialpage-example.com/kestrelbuild.nz

Font styles to use
Serif

Colors

Designer to choose colors to be used in the design.

Requirements
Must have
• Our new logo
• Our colours
• cfg logo

```html
<!DOCTYPE html>
<html lang="en">
<head>
<meta charset="utf-8">
<title>Kestrel Building Works – Business Card</title>
<link href="https://fonts.googleapis.com/css2?family=Playfair+Display:wght@400;700&family=Open+Sans:wght@400&display=swap" rel="stylesheet">
<style>
  :root {
    --navy: #15354f;
    --gold: #c9a06a;
    --white: #ffffff;
    --page: #f2f2f2;
  }
  * { box-sizing: border-box; margin: 0; padding: 0; }
  html, body { width: 1200px; height: 1200px; overflow: hidden; }
  body {
    background: var(--page);
    position: relative;
    font-family: "Open Sans", sans-serif;
  }
  .card {
    position: absolute;
    left: 160px;
    width: 880px;
    height: 520px;
    background: var(--navy);
    overflow: hidden;
    box-shadow: 0 6px 18px rgba(0,0,0,0.18);
  }
  .card--front { top: 60px; }
  .card--back { top: 620px; }

  .brand {
    font-family: "Playfair Display", serif;
    font-weight: 400;
    color: var(--white);
    text-transform: uppercase;
    text-align: center;
    line-height: 1.15;
    display: flex;
    flex-direction: column;
    align-items: center;
  }
  .brand__mark {
    width: 18px; height: 18px;
    border-radius: 50%;
    background: var(--gold);
    margin-bottom: 18px;
  }
  .card--front .brand {
    position: absolute;
    left: 0; right: 0; top: 170px;
    font-size: 46px;
    letter-spacing: 8px;
  }
  .card--back .brand {
    position: absolute;
    right: 60px; top: 60px;
    width: 340px;
    font-size: 28px;
    letter-spacing: 5px;
  }
  .card--back .brand__mark { width: 12px; height: 12px; margin-bottom: 12px; }

  .badge {
    position: absolute;
    right: 110px; top: 210px;
    width: 120px; height: 120px;
    border-radius: 50%;
    background: var(--white);
  }

  .person {
    position: absolute;
    left: 60px; top: 190px;
  }
  .person__name {
    font-family: "Playfair Display", serif;
    font-weight: 700;
    font-size: 38px;
    color: var(--gold);
  }
  .person__role {
    font-size: 22px;
    color: var(--white);
    margin-top: 2px;
  }

  .contacts {
    position: absolute;
    left: 60px; bottom: 50px;
    list-style: none;
  }
  .contacts__item {
    display: flex;
    align-items: center;
    gap: 14px;
    font-size: 22px;
    color: var(--white);
    line-height: 36px;
  }
  .contacts__icon { width: 18px; height: 18px; flex: none; }
  .contacts__square {
    width: 16px; height: 16px;
    background: var(--gold);
    flex: none;
    margin: 0 1px;
  }

  .gold-band {
    position: absolute;
    left: 0; right: 0; bottom: 14px;
    height: 8px;
    background: var(--gold);
  }
</style>
</head>
<body>

<section class="card card--front" aria-label="Card front">
  <div class="brand">
    <span class="brand__mark"></span>
    <span>Kestrel Building Works</span>
  </div>
</section>

<section class="card card--back" aria-label="Card back">
  <div class="brand">
    <span class="brand__mark"></span>
    <span>Kestrel Building Works</span>
  </div>

  <div class="badge" role="img" aria-label="Certified Framing Guild badge"></div>

  <div class="person">
    <p class="person__name">Malcolm Tivey</p>
    <p class="person__role">Director</p>
  </div>

  <ul class="contacts">
    <li class="contacts__item">
      <svg class="contacts__icon" viewBox="0 0 24 24" aria-hidden="true"><path fill="#c9a06a" d="M6.6 10.8a15 15 0 0 0 6.6 6.6l2.2-2.2c.3-.3.7-.4 1-.2 1.1.4 2.3.6 3.6.6.6 0 1 .4 1 1V20c0 .6-.4 1-1 1A17 17 0 0 1 3 4c0-.6.4-1 1-1h3.5c.6 0 1 .4 1 1 0 1.3.2 2.5.6 3.6.1.3 0 .7-.2 1z"/></svg>
      <span>0218845126</span>
    </li>
    <li class="contacts__item">
      <svg class="contacts__icon" viewBox="0 0 24 24" aria-hidden="true"><rect x="2" y="5" width="20" height="14" fill="none" stroke="#c9a06a" stroke-width="2"/><path d="M2 5l10 8 10-8" fill="none" stroke="#c9a06a" stroke-width="2"/></svg>
      <span>kestrelbuild.nz@maildrop-example.co.nz</span>
    </li>
    <li class="contacts__item">
      <svg class="contacts__icon" viewBox="0 0 24 24" aria-hidden="true"><g fill="none" stroke="#c9a06a" stroke-width="1.8"><circle cx="12" cy="12" r="10"/><ellipse cx="12" cy="12" rx="4.5" ry="10"/><path d="M2 12h20M4 7h16M4 17h16"/></g></svg>
      <span>www.kestrelbuildingworks-example.co.nz</span>
    </li>
    <li class="contacts__item">
      <span class="contacts__square"></span>
      <span>@kestrelbuild.nz</span>
    </li>
  </ul>

  <div class="gold-band"></div>
</section>

</body>
</html>
```